Design some Business Card for shipping company

We need a creative business card designed for a shipping company. All relevant information such as address and phone number can be found on our website. Will need a design for both front and back. The front will container our logo, slogan, contact information etc. The back will have a coupon and some text. check out www.taldovefreight.example for all the information. We need something memorable and unique that will stand out. It needs to a horizontal design. Not vertical.

```html
<!DOCTYPE html>
<html lang="en">
<head>
<meta charset="utf-8">
<title>Taldove Freight – Business Card</title>
<link rel="stylesheet" href="https://fonts.googleapis.com/css2?family=Roboto:wght@400;700;900&display=swap">
<style>
  :root {
    --bg: #ecebe8;
    --paper: #ffffff;
    --green: #1f7a45;
    --green-dark: #15603a;
    --red: #c8323a;
    --ink: #2b2b2b;
    --white: #ffffff;
  }
  html, body {
    margin: 0;
    padding: 0;
    width: 1200px;
    height: 912px;
    overflow: hidden;
    background: var(--bg);
    font-family: "Roboto", Arial, sans-serif;
  }
  .canvas {
    position: relative;
    width: 1200px;
    height: 912px;
  }
  .card {
    position: absolute;
    left: 290px;
    width: 620px;
    height: 354px;
    background: var(--paper);
    box-shadow: 0 6px 18px rgba(0,0,0,0.18);
    overflow: hidden;
  }
  .card--front { top: 70px; }
  .card--back { top: 488px; }
  .card__art {
    position: absolute;
    inset: 0;
  }
  .brand {
    position: absolute;
    display: flex;
    align-items: center;
    gap: 12px;
  }
  .brand__dot {
    width: 40px;
    height: 40px;
    border-radius: 50%;
    background: var(--green);
    flex: none;
  }
  .brand__name {
    font-weight: 900;
    font-size: 24px;
    letter-spacing: 0.5px;
    color: var(--green);
    line-height: 1;
  }
  .brand__slogan {
    font-weight: 700;
    font-size: 12px;
    color: var(--ink);
    margin-top: 4px;
  }
  .card--front .brand { left: 90px; top: 38px; }
  .card--back .brand { left: 150px; top: 140px; transform: scale(1.3); transform-origin: left center; }
  .person {
    position: absolute;
    left: 250px;
    top: 98px;
    width: 120px;
    text-align: center;
  }
  .person__name {
    font-size: 14px;
    color: var(--ink);
    letter-spacing: 0.5px;
  }
  .person__title {
    font-size: 12px;
    color: var(--green);
    margin-top: 2px;
  }
  .contact {
    position: absolute;
    font-size: 13px;
    color: var(--white);
    white-space: nowrap;
    transform: translateX(-50%);
  }
  .contact--address { left: 130px; top: 262px; }
  .contact--phone { left: 310px; top: 218px; }
  .contact--web { left: 500px; top: 178px; }
  .back-web {
    position: absolute;
    left: 330px;
    top: 232px;
    font-size: 14px;
    color: var(--green);
  }
</style>
</head>
<body>
<main class="canvas">

  <section class="card card--front" aria-label="Card front">
    <svg class="card__art" width="620" height="354" viewBox="0 0 620 354" aria-hidden="true">
      <polygon points="0,252 620,120 620,354 0,354" fill="var(--green)"/>
      <polygon points="0,340 620,340 620,354 0,354" fill="var(--green-dark)" opacity="0.35"/>
      <!-- home icon -->
      <g transform="translate(130 224)">
        <circle r="21" fill="var(--red)" stroke="var(--white)" stroke-width="3"/>
        <path d="M-9 1 L0 -8 L9 1 M-6 -1 V8 H-2 V3 H2 V8 H6 V-1" fill="none" stroke="var(--white)" stroke-width="2.4" stroke-linejoin="round"/>
      </g>
      <!-- phone icon -->
      <g transform="translate(310 186)">
        <circle r="21" fill="var(--red)" stroke="var(--white)" stroke-width="3"/>
        <path d="M-7 -8 L-3 -8 L-1 -3 L-4 -1 Q-1 4 3 5 L5 2 L9 4 L9 8 Q0 10 -6 3 Q-10 -3 -7 -8 Z" fill="var(--white)"/>
      </g>
      <!-- globe icon -->
      <g transform="translate(500 146)">
        <circle r="21" fill="var(--red)" stroke="var(--white)" stroke-width="3"/>
        <g fill="none" stroke="var(--white)" stroke-width="1.8">
          <circle r="9"/>
          <ellipse rx="4" ry="9"/>
          <line x1="-9" y1="0" x2="9" y2="0"/>
        </g>
      </g>
    </svg>

    <div class="brand">
      <span class="brand__dot"></span>
      <div>
        <div class="brand__name">TALDOVE FREIGHT</div>
        <div class="brand__slogan">Secure Affordable Shipping to Kenya</div>
      </div>
    </div>

    <div class="person">
      <div class="person__name">JHON DOE</div>
      <div class="person__title">Manager</div>
    </div>

    <div class="contact contact--address">Address line1, Adress line2</div>
    <div class="contact contact--phone">214 555 0142</div>
    <div class="contact contact--web">www.taldovefreight.example</div>
  </section>

  <section class="card card--back" aria-label="Card back">
    <div class="brand">
      <span class="brand__dot"></span>
      <div>
        <div class="brand__name">TALDOVE FREIGHT</div>
        <div class="brand__slogan">Secure Affordable Shipping to Kenya</div>
      </div>
    </div>
    <div class="back-web">www.taldovefreight.example</div>
  </section>

</main>
</body>
</html>
```